Home page web design for a lawn specialist business

-The design must be based around the attached HPID (home page information design) called Turf Tidings HPID. I've attached Word and PDF versions - these are the same. The table boxes are just for approximate placement of information and you can use boxes and bold shapes for this design.

All fonts used in the HPID are only examples - you can use any Google font you wish.

- Text that is in orange is for your information only. Text to go on the design is black. Some instructions are in the HPID. Please be creative!

-The design needs to be modern and exciting - colours are to be the green of the logo, and white ...and then choose dark green, or dark grey or black.

Logo - attached (it's not great quality but don't worry, we'll replace it later)

- I've provided the images for the galleries - they are labelled and will match the name in the HPID. Please use the supplied images!

- Examples of some websites that have great design... don't copy them please but they are similar in look to what we are after....
www.qmbbuildworks.co.nz
http://www.rim-safeguard.co.nz/
http://www.lumenhomes.wb.gs/

Important: Width of content will be 1280 pixels when implemented as a web page but the winning design will need to supplied be on a 2000 pixel wide background so nav bars and background can extend outside the 1280 width.
Header height (without nav bar) 150-160 pixels.

We don't comment on individual designs but will choose a winning design promptly.

Industry/Entity Type

Business

Number of Pages Required

1 page

Font styles to use
Sans Serif

Requirements
Must have
• clean, modern, well-spaced design

```html
<!DOCTYPE html>
<html lang="en">
<head>
<meta charset="utf-8">
<title>Turf Tidings – Lawn Specialists</title>
<link href="https://fonts.googleapis.com/css2?family=Oswald:wght@400;500&family=Open+Sans:wght@400;600;700&display=swap" rel="stylesheet">
<style>
:root{
  --green:#5aa21f;
  --green-dark:#2f7d1c;
  --green-bright:#7cc52a;
  --lime:#a8d43a;
  --ink:#1d1d1d;
  --dark:#222;
  --grey:#f1f1f1;
  --line:#dcdcdc;
  --text:#444;
  --white:#fff;
}
*{box-sizing:border-box;margin:0;padding:0}
html,body{width:1200px;height:2564px;overflow:hidden}
body{font-family:"Open Sans",Arial,sans-serif;color:var(--text);background:var(--white);position:relative}
.abs{position:absolute}

/* header */
.site-header{left:0;top:0;width:1200px;height:133px;background:var(--white)}
.brand{left:56px;top:14px;display:flex;align-items:center;gap:18px}
.brand-mark{width:100px;height:100px;border-radius:50%;background:var(--green-bright)}
.brand-name{font-family:"Oswald",sans-serif;font-size:38px;color:var(--green);font-weight:400}
.header-info{right:56px;top:10px;text-align:right}
.header-info .kicker{font-family:"Oswald",sans-serif;font-size:24px;line-height:1.2;color:var(--green);letter-spacing:1px}
.header-info .tag{font-size:13px;line-height:1.4;color:#666;margin-top:2px}
.header-info .region{font-size:13px;line-height:1.4;color:var(--green);font-weight:700;margin-top:10px}
.header-info .phone{font-family:"Oswald",sans-serif;font-size:30px;color:#333;line-height:1.1}

.main-nav{left:0;top:133px;width:1200px;height:41px;background:linear-gradient(#2b2b2b,#141414);display:flex;justify-content:center}
.main-nav a{color:#fff;text-decoration:none;font-size:15px;line-height:41px;padding:0 26px}
.main-nav a.current{color:var(--green-bright)}

/* slider */
.hero{left:0;top:174px;width:1200px;height:441px;background:linear-gradient(#eaf4dc,#cfe7a6)}
.hero-photo{left:56px;top:18px;width:1093px;height:403px;border:6px solid #fff;box-shadow:0 3px 10px rgba(0,0,0,.3);background:linear-gradient(100deg,#c9c1b6 0%,#8a6b55 35%,#7a5b45 48%,#3f8f25 52%,#64b03a 100%)}
.ba-label{top:366px;height:50px;line-height:50px;padding:0 18px;background:rgba(20,20,20,.8);color:#fff;font-family:"Oswald",sans-serif;font-size:34px;letter-spacing:1px}
.slide-arrow{top:190px;width:36px;height:40px;background:#222;display:flex;align-items:center;justify-content:center}

/* intro band */
.intro{left:0;top:615px;width:1200px;height:211px;background:linear-gradient(var(--green-bright),var(--green));text-align:center;color:#fff;overflow:hidden}
.intro h1{font-family:"Oswald",sans-serif;font-weight:400;font-size:36px;line-height:1.3;margin-top:18px}
.intro .sub{font-size:15px;line-height:1.4;font-weight:600;margin-top:2px}
.intro p{font-size:11.5px;line-height:1.8;width:1110px;margin:16px auto 0}

/* service cards */
.services{left:0;top:826px;width:1200px;height:302px;background:var(--grey)}
.card{width:520px;background:#fff;box-shadow:0 2px 6px rgba(0,0,0,.12)}
.card-title{height:54px;background:linear-gradient(var(--green-bright),var(--green-dark));color:#fff;font-family:"Oswald",sans-serif;font-size:32px;line-height:54px;padding-left:115px}
.card-icon{left:20px;top:-30px;width:82px;height:82px;border-radius:50%;background:#fff;border:4px solid var(--green);display:flex;align-items:center;justify-content:center}
.card-body{display:flex;gap:18px;padding:18px 20px 22px}
.card-img{width:232px;height:150px;flex:none}
.card-body p{font-size:12.5px;line-height:1.6;color:#444}
.btn{display:inline-block;background:#2a2a2a;color:#fff;font-size:11.5px;font-weight:600;padding:9px 14px;text-transform:uppercase;margin-top:16px;text-decoration:none;white-space:nowrap}

/* faq & gallery */
.sec-title{font-family:"Oswald",sans-serif;font-size:24px;color:var(--green-dark)}
.panel{background:#fff;box-shadow:0 2px 6px rgba(0,0,0,.15);padding:12px}
.text-link{font-size:12px;color:var(--green);font-weight:600;text-transform:uppercase}

/* video */
.video-intro{left:56px;top:1533px;font-size:14px;color:var(--green)}
.video{left:56px;top:1564px;width:539px;height:244px;background:linear-gradient(#b7b8b3,#6f8c4c 60%,#4f8e2a)}
.video-bar{left:0;bottom:0;width:539px;height:24px;background:#1b1b1b}
.play{left:250px;top:95px;width:46px;height:46px;border-radius:50%;background:#fff;display:flex;align-items:center;justify-content:center}
.about{left:686px;top:1540px;width:460px}
.about h2{font-family:"Oswald",sans-serif;font-weight:400;font-size:42px;color:var(--green)}
.about p{font-size:12.5px;line-height:1.6;margin-top:10px;color:#444}

/* testimonials */
.reviews{left:0;top:1841px;width:1200px;height:223px;background:linear-gradient(90deg,var(--green) 0%,var(--green-bright) 55%,#8cbf4a 75%,#4f7d2d 100%)}
.bubble{top:60px;width:320px;height:96px;background:#fff;border-radius:4px;padding:16px 36px;font-size:13px;font-style:italic;color:#444;line-height:1.5}
.bubble::after{content:"";position:absolute;left:30px;bottom:-14px;border:14px solid transparent;border-bottom:0;border-top-color:#fff}
.quote-mark{position:absolute;font-family:"Oswald",sans-serif;font-size:30px;color:var(--green);line-height:1}
.reviewer{top:174px;font-size:11.5px;color:#fff}
.reviewer b{color:#e9f6c9}

/* quote form */
.quote{left:0;top:2064px;width:1200px;height:300px;background:linear-gradient(#262626,#121212);text-align:center;color:#fff}
.quote h2{font-family:"Oswald",sans-serif;font-weight:400;font-size:30px;line-height:1.3;margin-top:18px}
.quote .lead{font-size:14px;line-height:1.4;color:var(--green-bright);font-style:italic;margin-top:2px}
.quote .lead b{font-family:"Oswald",sans-serif;font-style:normal;font-weight:400;font-size:22px}
.field{height:30px;background:#fff;border:1px solid #ccc;font-size:11px;color:#666;text-align:left;padding:7px 8px}
.send{left:550px;top:220px;width:98px;height:32px;background:var(--green);color:#fff;font-size:11px;font-weight:700;line-height:32px}
.quote-badge{right:90px;top:30px;width:160px;height:160px;border-radius:50%;background:#1f1f1f}

/* footer */
.site-footer{left:0;top:2364px;width:1200px;height:136px;background:#fff;text-align:center}
.footer-badge{left:572px;top:-30px;width:56px;height:56px;border-radius:50%;background:var(--green-bright);border:4px solid #fff;box-shadow:0 0 0 2px var(--green)}
.footer-nav{position:absolute;top:50px;width:100%;display:flex;justify-content:center;gap:28px;font-size:13px;color:#333}
.copyright{position:absolute;top:84px;width:100%;font-size:11px;color:#777}
.lawn-strip{left:0;top:2500px;width:1200px;height:64px;background:linear-gradient(#8fcb48,#3f8a1f)}
</style>
</head>
<body>

<header class="site-header abs">
  <div class="brand abs">
    <span class="brand-mark"></span>
    <span class="brand-name">Certificate in Turfcraft</span>
  </div>
  <div class="header-info abs">
    <div class="kicker">LAWN SPECIALISTS</div>
    <div class="tag">...from ground preparation to lawn aftercare</div>
    <div class="region">SERVICING THE AUCKLAND REGION</div>
    <div class="phone">0800 41 62 90</div>
  </div>
</header>

<nav class="main-nav abs">
  <a class="current">Home</a><a>About us</a><a>Services</a><a>Lawn care</a><a>Seasonal care</a><a>Hydroseeding</a><a>FAQs</a><a>Before &amp; After Gallery</a><a>Quote / Contact</a>
</nav>

<section class="hero abs">
  <div class="hero-photo abs" role="img" aria-label="Garden before and after new lawn: bare soil on the left, lush green grass on the right"></div>
  <div class="ba-label abs" style="left:472px">BEFORE</div>
  <div class="ba-label abs" style="left:606px">AFTER</div>
  <div class="slide-arrow abs" style="left:46px"><svg width="14" height="18"><path d="M11 2 3 9l8 7" fill="none" stroke="#fff" stroke-width="3"/></svg></div>
  <div class="slide-arrow abs" style="left:1118px"><svg width="14" height="18"><path d="M3 2l8 7-8 7" fill="none" stroke="#fff" stroke-width="3"/></svg></div>
</section>

<section class="intro abs">
  <h1>You can always spot an Turf Tidings lawn</h1>
  <div class="sub">It's the one that turns your neighbours green with envy.</div>
  <p>If you want a lawn or playing field that looks good throughout the year, talk to us. Turf Tidings are New Zealand's experts in high quality grass seeding and lawn maintenance, creating the lushest lawns you'll ever see. With high-tech equipment, years of experience and expert aftercare, nobody knows grass like Turf Tidings. There are many factors that influence the quality of a lawn, including seasonality, growing conditions, shade, seed types, and time. A one-size-fits-all solution couldn't possibly guarantee a great lawn, so we provide personalised advice, a full range of seeding techniques.</p>
</section>

<section class="services abs">
  <article class="card abs" style="left:56px;top:72px">
    <div class="card-icon abs"><svg width="44" height="36" viewBox="0 0 44 36"><path d="M4 24h36l-4 10H8z" fill="#333"/><path d="M8 24V8M14 24V4M20 24V9M26 24V3M32 24V8M38 24V12" stroke="#333" stroke-width="3"/></svg></div>
    <div class="card-title">Grass Seeding Services</div>
    <div class="card-body">
      <div class="card-img" role="img" aria-label="Freshly hydroseeded garden bed" style="background:linear-gradient(#7c8d5f,#2c7d6a)"></div>
      <div><p>With a wide range of grass seed applications to choose from, including hydroseeding and instant lawn, there is an option to suit your property and your requirements.</p><a class="btn">More about grass seeding</a></div>
    </div>
  </article>
  <article class="card abs" style="left:625px;top:72px">
    <div class="card-icon abs"><svg width="40" height="40" viewBox="0 0 40 40"><path d="M20 22v16M14 38h12" stroke="#333" stroke-width="4"/><path d="M20 20 6 6M20 20 34 6M20 20V3M20 20 3 16M20 20l17-4" stroke="#333" stroke-width="2" stroke-dasharray="3 2"/></svg></div>
    <div class="card-title">Lawn Care Maintenance</div>
    <div class="card-body">
      <div class="card-img" role="img" aria-label="Sprinkler watering a green lawn" style="background:linear-gradient(#6fa548,#2f6e22)"></div>
      <div><p>As well as lawn care services, the team at Turf Tidings provides helpful information for regular upkeep of your residential or commercial lawn.</p><a class="btn">More about ongoing lawn care</a></div>
    </div>
  </article>
</section>

<h2 class="sec-title abs" style="left:56px;top:1184px">FAQs about grass seeding and lawn care</h2>
<h2 class="sec-title abs" style="left:625px;top:1184px">Before and after lawn photos</h2>

<div class="panel abs" style="left:56px;top:1230px;width:520px;height:237px">
  <div role="img" aria-label="Large garden lawn with trees" style="width:496px;height:213px;background:linear-gradient(#9fb487,#4c8a2c 55%,#3c7a22)"></div>
  <div class="abs" style="left:50px;top:104px;color:#fff;font-size:13px;width:300px;line-height:1.4">For more information, read our frequently asked questions regarding grass seeding and lawn care.</div>
  <a class="btn abs" style="left:50px;top:150px">Grass seeding &amp; lawn care FAQs</a>
</div>

<div class="panel abs" style="left:625px;top:1230px;width:521px;height:210px">
  <div role="img" aria-label="Backyard before new lawn, bare ground" class="abs" style="left:12px;top:12px;width:246px;height:186px;background:linear-gradient(#b2ada2,#7d6e5b)"></div>
  <div role="img" aria-label="Same backyard after, lush green lawn" class="abs" style="left:263px;top:12px;width:246px;height:186px;background:linear-gradient(#a9b49a,#4a9a27)"></div>
  <div class="abs" style="left:12px;top:12px;width:497px;height:26px;background:rgba(20,20,20,.85);color:#fff;font-family:Oswald,sans-serif;font-size:15px;display:flex"><span style="flex:1;text-align:center;line-height:26px">BEFORE</span><span style="flex:1;text-align:center;line-height:26px">AFTER</span></div>
  <div class="abs" style="left:12px;top:162px;width:497px;height:36px;background:rgba(20,20,20,.7);color:#fff;font-size:11px;text-align:center;line-height:1.4;padding:3px 20px 0">See what you potential new lawn could look like by viewing a range of before and after lawn seeding photos.</div>
</div>
<div class="text-link abs" style="left:628px;top:1443px">Before and after photos ›</div>

<div class="video-intro abs">Watch the video on how Turf Tidings can transform your empty spaces into beautiful green grass lawns</div>
<div class="video abs" role="img" aria-label="Video of a house garden with a new green lawn">
  <div class="play abs"><svg width="18" height="20"><path d="M3 2l14 8-14 8z" fill="#222"/></svg></div>
  <div class="video-bar abs"><span style="position:absolute;left:4px;top:3px;width:18px;height:18px;background:var(--green)"></span><span style="position:absolute;left:36px;top:5px;font-size:10px;color:#ccc">04:59</span><span style="position:absolute;left:80px;top:11px;width:360px;height:3px;background:#555"></span></div>
</div>

<div class="about abs">
  <h2>Turf Tidings...</h2>
  <p>For all things grass, you need the best! Turf Tidings are skilled specialists when it comes to creating the perfect lawn for your property.</p>
  <p>From pre-seeding preparation to a full range of grass seeding services and lawn after care options, you'll enjoy a healthy green lawn for many years.</p>
  <p>Selling your property? Turf Tidings will add the wow factor to the outdoor areas of your home with a lush green lawn.</p>
  <a class="btn">Find out more</a>
</div>

<section class="reviews abs" role="img" aria-label="Green lawn and garden backdrop behind customer testimonials">
  <div class="bubble abs" style="left:56px"><span class="quote-mark" style="left:10px;top:8px">“</span>I would recommend Turf Tidings to anyone who wants an amazing lawn<span class="quote-mark" style="right:10px;bottom:-4px">”</span></div>
  <div class="bubble abs" style="left:430px"><span class="quote-mark" style="left:10px;top:8px">“</span>I would recommend Turf Tidings to anyone who wants an amazing lawn<span class="quote-mark" style="right:10px;bottom:-4px">”</span></div>
  <div class="bubble abs" style="left:826px"><span class="quote-mark" style="left:10px;top:8px">“</span>I would recommend Turf Tidings to anyone who wants an amazing lawn<span class="quote-mark" style="right:10px;bottom:-4px">”</span></div>
  <div class="reviewer abs" style="left:150px"><b>Ray Holloway</b> - Homeowner, Albany</div>
  <div class="reviewer abs" style="left:524px"><b>Ray Holloway</b> - Homeowner, Albany</div>
  <div class="reviewer abs" style="left:920px"><b>Ray Holloway</b> - Homeowner, Albany</div>
</section>

<section class="quote abs">
  <div class="quote-badge abs"></div>
  <h2>Get a quote for your new lawn!</h2>
  <div class="lead">Fill in the form or phone us on &nbsp;<b>0800 41 62 90.</b></div>
  <div class="field abs" style="left:195px;top:108px;width:195px">First Name</div>
  <div class="field abs" style="left:398px;top:108px;width:195px">Last Name</div>
  <div class="field abs" style="left:602px;top:108px;width:195px">Email Address</div>
  <div class="field abs" style="left:806px;top:108px;width:198px">Contact Phone</div>
  <div class="field abs" style="left:195px;top:144px;width:809px;height:46px">Details</div>
  <div class="send abs">CALL ME BACK</div>
</section>

<footer class="site-footer abs">
  <div class="footer-badge abs"></div>
  <div class="footer-nav"><span>Home</span><span>About Us</span><span>Services</span><span>Lawn care</span><span>Seasonal care</span><span>Hydroseeding</span><span>FAQs</span><span>Before &amp; After Gallery</span><span>Quote / Contact</span></div>
  <div class="copyright">© CERTIFICATE IN TURFCRAFT . All Rights Reserved 2015.</div>
</footer>
<div class="lawn-strip abs" role="img" aria-label="Strip of grass blades along the page bottom"></div>

</body>
</html>
```